church invitation for new individuals or families have moved into our area.

postcard inspiring people to attend our church and the benefits they will receive.
example: make new friends, become closer to God, like minded people, etc.
church info:
Bellwood Fellowship Baptist Church
4417 Co. Rd. 52
Carthage, MO 64836
Sunday school 10:00am
Worship 11:00am
need small map in lower right or left corner

Target Market(s)

new movers into our area

Industry/Entity Type

Church

Font styles to use
Decorative

Colors

Designer to choose colors to be used in the design.

Requirements
Must have
• Inspiring text message that will inspire individuals or families to drive 7 miles east of Carthage to attend our church. graphics ok if designer thinks necessary.
• use both sides of postcard except mail address area.
Nice to have
• You've found your home come and visit ours. God is not concerned about your past flops, failures or fumbles.
Should not have
• message should not sound like someone selling real estate, cars or merchandise.

```html
<!DOCTYPE html>
<html lang="en">
<head>
<meta charset="utf-8">
<title>Bellwood Fellowship Baptist Church – Welcome Postcard</title>
<link rel="stylesheet" href="https://fonts.googleapis.com/css2?family=Great+Vibes&family=Cinzel:wght@400;600&family=Roboto+Condensed:wght@700&family=Roboto:ital,wght@0,400;0,500;1,300&display=swap">
<style>
  :root {
    --stage: #96979a;
    --ink-deep: #0b1418;
    --teal-dark: #123a44;
    --teal: #1f6f7c;
    --teal-glow: #5fd1d6;
    --band: #0f7f8c;
    --panel: #f4f4f4;
    --paper: #ffffff;
    --text: #1d1d1d;
    --muted: #6b6b6b;
    --rule: #e6e6e6;
    --map-land: #e9e6df;
  }
  * { box-sizing: border-box; margin: 0; padding: 0; }
  html, body { width: 811px; height: 1200px; overflow: hidden; }
  body { background: var(--stage); position: relative; font-family: "Roboto", sans-serif; }

  .card { position: absolute; left: 80px; width: 651px; height: 501px; box-shadow: 0 2px 6px rgba(0,0,0,.25); overflow: hidden; }

  /* Front */
  .card--front { top: 80px; }
  .front__photo {
    position: absolute; inset: 0;
    background:
      radial-gradient(ellipse 60% 45% at 85% 10%, rgba(120,200,255,.55), transparent 70%),
      radial-gradient(ellipse 55% 50% at 55% 40%, rgba(60,170,170,.55), transparent 75%),
      linear-gradient(180deg, transparent 74%, #3a2414 82%, #1a0f08 100%),
      linear-gradient(120deg, var(--ink-deep) 0%, var(--teal-dark) 45%, #1c4f5a 70%, #2a5f7a 100%);
  }
  .front__headline {
    position: absolute; left: 0; right: 0; top: 155px;
    text-align: center; color: #fff; font-family: "Great Vibes", cursive; font-weight: 400;
    white-space: nowrap; line-height: 1;
  }
  .front__headline .lead { font-size: 70px; }
  .front__headline .emph { font-size: 118px; margin-left: 4px; }
  .front__tagline {
    position: absolute; left: 0; right: 0; top: 462px; text-align: center;
    color: #fff; font-family: "Cinzel", serif; font-size: 12px; letter-spacing: .2px;
    font-variant: small-caps;
  }

  /* Back */
  .card--back { top: 621px; background: var(--paper); }
  .back__info { position: absolute; left: 0; top: 0; width: 314px; height: 418px; }
  .back__hero {
    position: absolute; left: 0; top: 0; width: 314px; height: 233px;
    background:
      radial-gradient(ellipse 70% 50% at 40% 20%, rgba(95,209,214,.55), transparent 70%),
      linear-gradient(160deg, var(--teal) 0%, var(--teal-dark) 50%, var(--ink-deep) 100%);
  }
  .back__welcome {
    position: absolute; left: 0; right: 0; top: 20px; text-align: center;
    color: #fff; font-family: "Great Vibes", cursive; font-size: 44px; line-height: 42px;
  }
  .back__details { position: absolute; left: 0; top: 233px; width: 314px; height: 147px; background: var(--panel); }
  .back__map {
    position: absolute; left: 12px; top: 173px; width: 290px; height: 120px;
    border-radius: 8px; background: linear-gradient(135deg, var(--map-land), #dedad1);
    box-shadow: 0 1px 3px rgba(0,0,0,.2);
  }
  .back__name { position: absolute; left: 0; right: 0; top: 305px; text-align: center;
    font-family: "Roboto Condensed", sans-serif; font-weight: 700; font-size: 17px; color: var(--text); }
  .back__address { position: absolute; left: 0; right: 0; top: 328px; text-align: center; font-size: 14px; color: var(--text); }
  .back__note { position: absolute; left: 0; right: 0; top: 350px; text-align: center; font-size: 12px; font-style: italic; font-weight: 300; color: var(--muted); }
  .back__times {
    position: absolute; left: 0; top: 380px; width: 314px; height: 38px; background: var(--band);
    color: #fff; font-family: "Roboto Condensed", sans-serif; font-weight: 700; font-size: 15px;
    display: flex; align-items: center; justify-content: center; gap: 8px;
  }
  .stamp-box { position: absolute; left: 562px; top: 25px; width: 65px; height: 76px; border: 1px solid var(--rule); }
  .address-line { position: absolute; left: 338px; width: 289px; height: 2px; background: var(--rule); }
</style>
</head>
<body>
  <section class="card card--front">
    <div class="front__photo" role="img" aria-label="Open Bible on a wooden table under soft teal light rays"></div>
    <h1 class="front__headline"><span class="lead">stay close to</span><span class="emph">God</span></h1>
    <p class="front__tagline">God is not concerned about your past flops, failures or fumbles...</p>
  </section>

  <section class="card card--back">
    <div class="back__info">
      <div class="back__hero" role="img" aria-label="Soft teal light texture"></div>
      <h2 class="back__welcome">You’ve found<br>your home come<br>and visit ours!</h2>
      <div class="back__details"></div>
      <div class="back__map" role="img" aria-label="Map showing the church location east of Carthage on County Road 52"></div>
      <p class="back__name">Bellwood Fellowship Baptist Church</p>
      <p class="back__address">4417 Co. Rd. 52, Carthage, MO 64836</p>
      <p class="back__note">*7 miles east of Downtown Carthage</p>
      <p class="back__times"><span>Sunday School 10:00am</span><span>•</span><span>Worship 11:00am</span></p>
    </div>
    <div class="stamp-box"></div>
    <div class="address-line" style="top:270px"></div>
    <div class="address-line" style="top:320px"></div>
    <div class="address-line" style="top:369px"></div>
  </section>
</body>
</html>
```